Business cards for law firm with global theme

I'd like business cards with contact info for two offices. They should include the colors and font of the new logo design, which is a stylized globe with an "F" in it. The feel should be very modern and professional.

```html
<!DOCTYPE html>
<html lang="en">
<head>
<meta charset="utf-8">
<title>Valmora Law – Business Cards</title>
<link href="https://fonts.googleapis.com/css2?family=Open+Sans:wght@400;600;700&display=swap" rel="stylesheet">
<style>
  :root {
    --navy-deep: #062a55;
    --navy: #0c3d70;
    --navy-mid: #14558f;
    --sky: #1e9be0;
    --paper: #f1f3f6;
    --ink-light: #ffffff;
    --stage: #e4e6ea;
  }
  * { box-sizing: border-box; margin: 0; padding: 0; }
  html, body {
    width: 1200px; height: 768px; overflow: hidden;
    background: var(--stage);
    font-family: "Open Sans", Arial, sans-serif;
  }
  .sheet {
    width: 1200px; height: 768px;
    display: flex; align-items: center; justify-content: center; gap: 40px;
  }
  .card {
    position: relative;
    width: 560px; height: 320px;
    border-radius: 22px;
    overflow: hidden;
    box-shadow: 0 10px 28px rgba(6, 42, 85, 0.25);
  }

  /* Back of card */
  .card-back {
    background: linear-gradient(135deg, var(--navy-mid) 0%, var(--navy) 45%, var(--navy-deep) 100%);
    display: flex; align-items: center; justify-content: center;
  }
  .brand { display: flex; align-items: center; gap: 22px; }
  .brand-dot {
    width: 78px; height: 78px; border-radius: 50%;
    background: var(--sky);
  }
  .brand-name {
    display: flex; flex-direction: column; align-items: center;
    font-weight: 700; color: var(--ink-light);
    letter-spacing: 1px; line-height: 1;
  }
  .brand-name .word { font-size: 38px; }
  .brand-name .sub {
    display: flex; align-items: center; gap: 8px;
    font-size: 20px; margin-top: 4px; width: 100%;
  }
  .brand-name .sub::before, .brand-name .sub::after {
    content: ""; flex: 1; height: 1.5px; background: var(--sky);
  }

  /* Front of card */
  .card-front { background: var(--navy); }
  .card-front .panel { position: absolute; inset: 0; }
  .card-front .brand {
    position: absolute; left: 22px; top: 64px; width: 190px;
    flex-direction: column; gap: 12px;
  }
  .card-front .brand-dot { width: 62px; height: 62px; background: var(--sky); }
  .card-front .brand-name { color: var(--navy-deep); }
  .card-front .brand-name .word { font-size: 29px; }
  .card-front .brand-name .sub { font-size: 17px; }

  .details {
    position: absolute; left: 300px; top: 40px; right: 16px;
    color: var(--ink-light); font-size: 13px; line-height: 1.3;
  }
  .person-name { color: var(--sky); font-size: 21px; font-weight: 700; }
  .person-role { font-size: 13px; margin-bottom: 8px; }
  .address { margin-bottom: 6px; }
  .address:last-of-type { margin-bottom: 8px; }
  .contact-list { list-style: none; }
  .contact-list li { display: flex; align-items: center; gap: 8px; height: 18px; }
  .contact-list svg { width: 12px; height: 12px; flex: none; fill: var(--ink-light); }
</style>
</head>
<body>
<main class="sheet">

  <section class="card card-back" aria-label="Card back">
    <div class="brand">
      <span class="brand-dot"></span>
      <div class="brand-name">
        <span class="word">VALMORA</span>
        <span class="sub">LAW</span>
      </div>
    </div>
  </section>

  <section class="card card-front" aria-label="Card front">
    <svg class="panel" viewBox="0 0 560 320" preserveAspectRatio="none" aria-hidden="true">
      <defs>
        <linearGradient id="blueSide" x1="0" y1="0" x2="1" y2="1">
          <stop offset="0" stop-color="#14558f"/>
          <stop offset="1" stop-color="#0a3566"/>
        </linearGradient>
      </defs>
      <rect width="560" height="320" fill="url(#blueSide)"/>
      <path d="M0 0 H282 C272 140 220 250 112 320 H0 Z" fill="#1e9be0"/>
      <path d="M0 0 H274 C264 140 212 250 100 320 H0 Z" fill="#f1f3f6"/>
    </svg>

    <div class="brand">
      <span class="brand-dot"></span>
      <div class="brand-name">
        <span class="word">VALMORA</span>
        <span class="sub">LAW</span>
      </div>
    </div>

    <div class="details">
      <p class="person-name">Daniel Hartley</p>
      <p class="person-role">Managing Director</p>
      <p class="address">4120 Birchwood Lane<br>Juneau, Alaska 99801</p>
      <p class="address">2875 Harbor View Drive<br>Seattle, Washington 98121</p>
      <ul class="contact-list">
        <li><svg viewBox="0 0 16 16"><path d="M3 1l3 3-2 2c1 2 3 4 5 5l2-2 3 3-2 3C7 15 1 9 1 3z"/></svg>555-214-7730</li>
        <li><svg viewBox="0 0 16 16"><path d="M4 0h8v16H4z M5.5 2v10h5V2z"/></svg>555-382-4196</li>
        <li><svg viewBox="0 0 16 16"><path d="M4 1h8v4H4z M1 6h14v7H1z M4 11h8v4H4z"/></svg>555-907-6158</li>
        <li><svg viewBox="0 0 16 16"><path d="M1 3h14v10H1z M2 4l6 5 6-5v-.5H2z" fill-rule="evenodd"/></svg>info@valmoralaw.com</li>
        <li><svg viewBox="0 0 16 16"><circle cx="8" cy="8" r="7"/></svg>www.valmoralaw.com</li>
      </ul>
    </div>
  </section>

</main>
</body>
</html>
```